Criação de Papelaria (6 itens) para Brisa & Lajedo
" Prestamos serviços de outorga e licenças ambientais, análise de água, aproveitamento de águas, pesquisa de água mineral, poços artesianos (furação, recuperação, tratamento de água), energia solar, etc. "

```html
<!DOCTYPE html>
<html lang="pt-BR">
<head>
<meta charset="UTF-8">
<title>Brisa &amp; Lajedo — Papel Timbrado</title>
<link rel="stylesheet" href="https://fonts.googleapis.com/css2?family=Arimo:wght@400;700&display=swap">
<style>
  :root {
    --backdrop: #d6d6d6;
    --paper: #ffffff;
    --brand-blue: #2a4d9c;
    --brand-blue-light: #4f74c2;
    --brand-green: #5a9e2f;
    --ink: #3a3a3a;
    --ink-soft: #777777;
  }
  * { margin: 0; padding: 0; box-sizing: border-box; }
  html, body {
    width: 1200px;
    height: 1200px;
    overflow: hidden;
    background: var(--backdrop);
    font-family: "Arimo", Arial, sans-serif;
  }
  .canvas {
    width: 1200px;
    height: 1200px;
    display: flex;
    align-items: center;
    justify-content: center;
  }
  .letterhead {
    position: relative;
    width: 778px;
    height: 1100px;
    background: var(--paper);
    box-shadow: 0 6px 24px rgba(0, 0, 0, 0.18);
    overflow: hidden;
  }
  .letterhead__brand {
    position: absolute;
    top: 60px;
    left: 0;
    right: 0;
    text-align: center;
  }
  .brand-name {
    display: inline-flex;
    align-items: center;
    gap: 8px;
    font-size: 26px;
    font-weight: 700;
    color: var(--brand-blue);
    letter-spacing: 0.5px;
  }
  .brand-name__dot {
    width: 12px;
    height: 12px;
    border-radius: 50%;
    background: var(--brand-green);
  }
  .brand-tagline {
    margin-top: 4px;
    font-size: 10px;
    color: var(--brand-green);
    letter-spacing: 1.5px;
    text-transform: uppercase;
  }
  .letterhead__contact {
    position: absolute;
    left: 160px;
    right: 60px;
    bottom: 96px;
    font-size: 12px;
    color: var(--ink);
    line-height: 1.45;
  }
  .contact-row {
    display: flex;
    justify-content: flex-end;
    gap: 40px;
  }
  .contact-col { text-align: right; }
  .contact-address {
    margin-top: 2px;
    text-align: right;
  }
  .letterhead__band {
    position: absolute;
    left: 0;
    bottom: 0;
    width: 100%;
    height: 80px;
  }
</style>
</head>
<body>
  <main class="canvas">
    <article class="letterhead">
      <header class="letterhead__brand">
        <div class="brand-name"><span class="brand-name__dot"></span>Brisa &amp; Lajedo</div>
        <div class="brand-tagline">Soluções Ambientais</div>
      </header>

      <footer class="letterhead__contact">
        <div class="contact-row">
          <div class="contact-col">
            <div>(00) 0000-0000</div>
            <div>www.brisaelajedo.com.br</div>
          </div>
          <div class="contact-col">
            <div>(00) 00000-0000</div>
            <div>contato@brisaelajedo.com.br</div>
          </div>
        </div>
        <div class="contact-address">Rua das Acácias nº 120 - Vila Serena - Campinas - SP - 13010-200</div>
      </footer>

      <svg class="letterhead__band" viewBox="0 0 778 80" preserveAspectRatio="none" aria-hidden="true">
        <path d="M0 30 C 260 58, 520 34, 778 8 L 778 80 L 0 80 Z" fill="var(--brand-blue-light)"/>
        <path d="M0 38 C 260 66, 520 42, 778 16 L 778 80 L 0 80 Z" fill="var(--brand-blue)"/>
      </svg>
    </article>
  </main>
</body>
</html>
```